WEB PAGES DESIGN

We need a web design for a new company called "NEXO47". Our major business is that provide Internet Data Center solution, such as: rack/colocation, bandwidth, dedicated server, cloud server, CDN, and so on.
Requirements of Design:
1. Home page layout can refer to index-content.jpg in the attachments, but not limited.
2. According to match logo colors to design colors of web pages, Logo in the attachments.
3. The web contents of home page in image of the index-content.jpg.
4. The successful bidder will need to design three banner.

```html
<!DOCTYPE html>
<html lang="en">
<head>
<meta charset="utf-8">
<title>NEXO47 – IDC Solutions</title>
<link rel="stylesheet" href="https://fonts.googleapis.com/css2?family=Open+Sans:ital,wght@0,400;0,600;0,700;1,400&display=swap">
<style>
:root{
  --green:#8db12e;
  --green-dark:#6f8e1f;
  --ink:#3a3a3a;
  --muted:#666;
  --line:#7a5a3a;
  --frame:#d8d8d8;
  --badge:#e4e4e4;
  --footer:#2b2b2b;
  --footer-base:#1c1c1c;
  --footer-text:#c9c9c9;
  --footer-dim:#8a8a8a;
}
*{margin:0;padding:0;box-sizing:border-box}
html,body{width:771px;height:1200px;overflow:hidden;background:#fff}
body{font-family:"Open Sans",Arial,sans-serif;color:var(--ink);position:relative}
.abs{position:absolute}

.site-header{position:absolute;left:0;top:0;width:771px;height:55px;background:#fff;border-bottom:1px solid #e4e4e4}
.brand{left:64px;top:17px;display:flex;align-items:center;gap:7px;font-weight:700;font-size:15px;color:var(--ink)}
.brand-mark{width:16px;height:16px;background:var(--green)}
.main-nav a{position:absolute;top:22px;font-size:9px;color:#555;text-decoration:none;transform:translateX(-50%);white-space:nowrap}

.hero{left:0;top:55px;width:771px;height:328px;
  background:
    radial-gradient(ellipse 120px 150px at 415px 130px,rgba(170,170,170,.55),rgba(170,170,170,0) 100%),
    radial-gradient(ellipse 190px 220px at 430px 290px,rgba(40,40,40,.9),rgba(40,40,40,0) 100%),
    radial-gradient(ellipse 160px 120px at 640px 200px,rgba(120,120,120,.45),rgba(120,120,120,0) 100%),
    linear-gradient(90deg,#3a3a3a 0%,#555 35%,#4a4a4a 60%,#3c3c3c 100%)}
.hero-title{left:66px;top:143px;font-size:38px;line-height:44px;font-weight:400;color:#fff;letter-spacing:-.3px}
.hero-text{left:70px;top:193px;width:262px;font-size:11.3px;line-height:18.4px;color:#eee}
.hero-btn{left:70px;top:261px;width:107px;height:39px;background:var(--green);border-bottom:3px solid var(--green-dark);color:#fff;font-size:10px;font-weight:700;display:flex;align-items:center;justify-content:center}
.hero-arrow{width:22px;height:22px;border-radius:50%;background:rgba(255,255,255,.12);display:flex;align-items:center;justify-content:center}

.section-title{left:0;width:771px;text-align:center;font-size:16px;font-weight:700;color:var(--ink);letter-spacing:.3px}
.section-rule{left:338px;width:95px;height:2px;background:var(--line)}
.section-lead{left:0;width:771px;text-align:center;font-size:8.6px;color:var(--muted)}

.product{top:508px;width:192.75px}
.product-photo{height:127px}
.product-name{margin-top:12px;text-align:center;font-size:9.6px;font-weight:700;color:var(--ink)}
.product-link{margin-top:3px;text-align:center;font-size:7.6px;font-style:italic;color:var(--muted)}

.partner{top:814px;width:143px;height:86px;border:2px solid var(--frame);display:flex;align-items:center;justify-content:center}
.partner-badge{width:86px;height:26px;background:var(--badge);border-radius:13px}
.partner-arrow{top:858px;width:8px;height:8px;border-radius:50%;background:#c9c9c9}

.site-footer{left:0;top:936px;width:771px;height:232px;background:var(--footer)}
.footer-head{font-size:7.5px;font-weight:700;color:#fff;letter-spacing:.2px}
.news-item{left:64px;width:200px}
.news-title{font-size:8px;color:#eee;font-weight:400}
.news-date{margin-top:5px;font-size:6.5px;font-style:italic;color:var(--footer-dim)}
.footer-brand{left:290px;top:1002px;width:120px;display:flex;align-items:center;justify-content:center;gap:8px;font-size:22px;font-weight:700;color:var(--green);white-space:nowrap}
.footer-brand-mark{flex:none;width:20px;height:20px;background:var(--green)}
.footer-links{left:456px;top:992px;list-style:none}
.footer-links li{font-size:7px;color:var(--footer-text);height:16px}
.contact-line{font-size:7px;color:var(--footer-text);display:flex;align-items:center;gap:6px}
.social-label{left:326px;top:1115px;font-size:7.5px;color:#fff}
.social-dot{top:1111px;width:18px;height:18px;border-radius:50%;background:#4a4a4a}
.talk{left:596px;top:1102px;display:flex;align-items:center;gap:8px}
.talk-ring{width:38px;height:38px;border-radius:50%;border:2px solid var(--green);display:flex;align-items:center;justify-content:center}
.talk-name{font-size:14px;font-weight:700;color:var(--green)}

.footer-base{left:0;top:1168px;width:771px;height:32px;background:var(--footer-base);text-align:center;font-size:7px;color:var(--footer-dim);line-height:32px}
</style>
</head>
<body>

<header class="site-header">
  <div class="abs brand"><span class="brand-mark"></span>NEXO47</div>
  <nav class="main-nav">
    <a style="left:318px">Home</a>
    <a style="left:412px">Dedicated server</a>
    <a style="left:509px">Hosting</a>
    <a style="left:598px">Data Centers</a>
    <a style="left:690px">About Us</a>
  </nav>
</header>

<section class="abs hero" role="img" aria-label="Banner photo: engineer in glasses against a dark background of glowing data security words"></section>
<h1 class="abs hero-title">IDC Solutions</h1>
<p class="abs hero-text">NEXO47 provides a wide range of highly specialized solutions that utilizes technology to transform your organization.</p>
<div class="abs hero-btn">LEARN MORE</div>
<div class="abs hero-arrow" style="left:24px;top:201px"><svg width="8" height="10" viewBox="0 0 8 10"><path d="M6 1 2 5l4 4" fill="none" stroke="#888" stroke-width="1.5"/></svg></div>
<div class="abs hero-arrow" style="left:729px;top:201px"><svg width="8" height="10" viewBox="0 0 8 10"><path d="M2 1l4 4-4 4" fill="none" stroke="#888" stroke-width="1.5"/></svg></div>

<h2 class="abs section-title" style="top:424px">PRODUCT LIST</h2>
<div class="abs section-rule" style="top:454px"></div>
<p class="abs section-lead" style="top:471px">Lorem Ipsum is simply dummy text of the printing and typesetting industry has been the industry's standard.</p>

<div class="abs product" style="left:0">
  <div class="product-photo" role="img" aria-label="Photo of dark server cabinets in a data hall" style="background:radial-gradient(ellipse 70px 60px at 115px 70px,#2a2c30,rgba(42,44,48,0)),linear-gradient(180deg,#d4d6d8 0%,#a9abad 30%,#5b5d60 55%,#8e9092 80%,#c4c5c6 100%)"></div>
  <div class="product-name">DEDICATED SERVERS</div>
  <div class="product-link">Click here for details</div>
</div>
<div class="abs product" style="left:192.75px">
  <div class="product-photo" role="img" aria-label="Photo of a man working at a laptop" style="background:radial-gradient(ellipse 60px 70px at 140px 75px,#6b6a52,rgba(107,106,82,0)),radial-gradient(ellipse 30px 20px at 25px 105px,#cfd8d8,rgba(207,216,216,0)),linear-gradient(160deg,#55626a,#36434a 55%,#2a3336)"></div>
  <div class="product-name">SERVERS HOSTING</div>
  <div class="product-link">Click here for details</div>
</div>
<div class="abs product" style="left:385.5px">
  <div class="product-photo" role="img" aria-label="Photo of a technician wiring network cables" style="background:radial-gradient(ellipse 50px 40px at 50px 105px,#d9cdb8,rgba(217,205,184,0)),radial-gradient(ellipse 60px 70px at 150px 60px,#4f6a7c,rgba(79,106,124,0)),linear-gradient(135deg,#2f3338,#575c63 50%,#7a7560)"></div>
  <div class="product-name">RACK &amp; BANDWIDTH</div>
  <div class="product-link">Click here for details</div>
</div>
<div class="abs product" style="left:578.25px">
  <div class="product-photo" role="img" aria-label="Photo of a businessman standing in a bright server room" style="background:radial-gradient(ellipse 14px 45px at 96px 75px,#3a3f48,rgba(58,63,72,0)),linear-gradient(90deg,#7e8c9a 0%,#c8d3dc 22%,#eef2f5 50%,#c8d3dc 78%,#8a97a4 100%)"></div>
  <div class="product-name">RESELLER &amp; REFERRAL</div>
  <div class="product-link">Click here for details</div>
</div>

<h2 class="abs section-title" style="top:722px">OUR PARTNERS</h2>
<div class="abs section-rule" style="top:752px"></div>
<p class="abs section-lead" style="top:768px">Lorem Ipsum is simply dummy text of the printing and typesetting industry has been the industry's standard.</p>

<div class="abs partner-arrow" style="left:47px"></div>
<div class="abs partner" style="left:64px"><span class="partner-badge"></span></div>
<div class="abs partner" style="left:231px"><span class="partner-badge"></span></div>
<div class="abs partner" style="left:398px"><span class="partner-badge"></span></div>
<div class="abs partner" style="left:565px"><span class="partner-badge"></span></div>
<div class="abs partner-arrow" style="left:720px"></div>

<footer class="abs site-footer"></footer>
<div class="abs footer-head" style="left:63px;top:973px">LATEST NEWS</div>
<svg class="abs" style="left:242px;top:973px" width="14" height="8" viewBox="0 0 14 8"><path d="M4 1 1 4l3 3M10 1l3 3-3 3" fill="none" stroke="#999" stroke-width="1"/></svg>
<div class="abs news-item" style="top:999px"><div class="news-title">Lorem Ipsum is simply dummy text of the printing</div><div class="news-date">Posted on 27 March 2015</div></div>
<div class="abs news-item" style="top:1038px"><div class="news-title">Lorem Ipsum is simply dummy text of the printing</div><div class="news-date">Posted on 27 March 2015</div></div>
<div class="abs news-item" style="top:1076px"><div class="news-title">Lorem Ipsum is simply dummy text of the printing</div><div class="news-date">Posted on 27 March 2015</div></div>
<div class="abs news-item" style="top:1116px"><div class="news-title">Lorem Ipsum is simply dummy text of the printing</div><div class="news-date">Posted on 27 March 2015</div></div>

<div class="abs footer-brand"><span class="footer-brand-mark"></span>NEXO47</div>

<div class="abs footer-head" style="left:456px;top:973px">WELCOME</div>
<ul class="abs footer-links">
  <li>Home</li><li>Dedicated server</li><li>Hosting</li><li>Data Centers</li><li>About Us</li>
</ul>

<div class="abs footer-head" style="left:593px;top:973px">CONTACT INFO</div>
<div class="abs" style="left:593px;top:991px;font-size:7px;line-height:16px;color:var(--footer-text)">120 Street name, City name,<br>City name, zip code : 4100210</div>
<div class="abs contact-line" style="left:594px;top:1027px"><svg width="8" height="8" viewBox="0 0 8 8"><path d="M1 1h2l1 2-1 1a4 4 0 0 0 2 2l1-1 2 1v2A7 7 0 0 1 1 1z" fill="#999"/></svg>( 3100 ) 555 014</div>
<div class="abs contact-line" style="left:594px;top:1046px"><svg width="8" height="8" viewBox="0 0 8 8"><path d="M1 5V4a3 3 0 0 1 6 0v1" fill="none" stroke="#999"/><rect x="0.5" y="4.5" width="2" height="3" fill="#999"/><rect x="5.5" y="4.5" width="2" height="3" fill="#999"/></svg>Live Chat</div>
<div class="abs contact-line" style="left:594px;top:1065px"><svg width="9" height="8" viewBox="0 0 9 8"><rect x="1.5" y="1" width="6" height="4" fill="none" stroke="#999"/><path d="M0 7h9" stroke="#999"/></svg>Support Online</div>

<div class="abs social-label">Connect with our social network :</div>
<div class="abs social-dot" style="left:451px"></div>
<div class="abs social-dot" style="left:474px"></div>
<div class="abs social-dot" style="left:498px"></div>
<div class="abs social-dot" style="left:521px"></div>
<div class="abs social-dot" style="left:544px"></div>

<div class="abs talk"><span class="talk-ring"><svg width="16" height="14" viewBox="0 0 16 14"><path d="M2 6a6 4.5 0 1 1 3 4l-3 2 1-3A5 5 0 0 1 2 6z" fill="none" stroke="#8db12e" stroke-width="1.6"/></svg></span><span class="talk-name">TALKWAVE</span></div>

<div class="abs footer-base">© 2015. Nexo 47. All rights reserved. &nbsp;&nbsp; Trms of Service &nbsp;&nbsp; / &nbsp;&nbsp; Privacy Policy</div>

</body>
</html>
```